Craft brewery, Name a beer competition - Poster

We are a New Zealand craft brewery, based in Auckland. We are running a competition to name our newest craft beer.
We run an on-site brewery at a bar and restaurant, called The Brewhouse Kestrelgate, offering a range of 8 of our own craft beers on tap as well as some guest beers. We offer a permanent range as well as some seasonal beers.
We like to experiment and have fun which shows in some of our creations like Ember Drift (a smoked chilli beer) or Zorra (an alcoholic ginger beer). www.thebrewhousekestrelgate.co.nz
With this competition we would like to engage with the Auckland community, not just craft beer lovers, but those who are just learning about craft beer versus commercial products.

Hi there,

All the designers who have received feedback on their first designs are already aware that we have shortened the copy for the poster. For those of you who haven't seen the communication yet, I have uploaded a revised copy to the brief section (file: Beer naming competition_poster_shortened.docx)

Thank you!

Reason: A few of the designs are really close so we feel that within a couple more days we should be able to refine them and find the perfect design. Thank you all for your continued effort!

Target Market(s)

25-45 year old urban craft beer lover or those who would like to learn more about craft beer, male and female

Industry/Entity Type

Brewery

Requirements
Must have
• A3 poster, following requirements from the printer.
Layout: http://www.0800quillark.co.nz/printing/layout
File Format: http://www.0800quillark.co.nz/printing/formats

The company logo should be incorporated, the poster should be catchy, fun and engaging in order to get a high participation rate in our competition.

Copy as per briefing document attached.

```html
<!DOCTYPE html>
<html lang="en">
<head>
<meta charset="utf-8">
<title>Name Our Newest Craft Beer – The Brewhouse Kestrelgate</title>
<link href="https://fonts.googleapis.com/css2?family=Open+Sans:wght@300;400;600;700&family=Open+Sans+Condensed:wght@300&family=Lobster&family=Montserrat:wght@700&display=swap" rel="stylesheet">
<style>
  :root {
    --frame: #f3f2ea;
    --ink: #000000;
    --white: #ffffff;
    --gold: #e8a923;
    --leather-light: #c9913f;
    --leather-mid: #a8702c;
    --leather-dark: #6e4419;
    --stamp: #5a3412;
    --band-light: #8a6a35;
    --band-dark: #2a1e0c;
  }
  * { margin: 0; padding: 0; box-sizing: border-box; }
  html, body {
    width: 849px; height: 1200px; overflow: hidden;
    background: var(--frame);
  }
  .poster {
    position: relative;
    width: 849px; height: 1200px;
    background: var(--frame);
    padding: 9px;
    font-family: "Open Sans", Arial, sans-serif;
  }
  .panel {
    position: relative;
    width: 100%; height: 100%;
    background: var(--ink);
    overflow: hidden;
    color: var(--white);
    text-align: center;
  }
  .light-streaks {
    position: absolute;
    left: -120px; top: 360px;
    width: 1100px; height: 330px;
    transform: rotate(-38deg);
    transform-origin: center;
    background: linear-gradient(180deg,
      rgba(0,0,0,0) 0%,
      rgba(140,120,50,0.35) 22%,
      rgba(60,120,60,0.45) 40%,
      rgba(60,110,140,0.45) 58%,
      rgba(90,50,130,0.4) 76%,
      rgba(0,0,0,0) 100%);
    filter: blur(14px);
  }
  .brand {
    position: absolute;
    top: 52px; left: 0; right: 0;
    display: flex; justify-content: center; align-items: center; gap: 8px;
    font-weight: 400; font-size: 11px; letter-spacing: 3px;
    text-transform: uppercase; color: var(--white);
  }
  .brand-dot {
    width: 9px; height: 9px; border: 1px solid var(--white); border-radius: 50%;
  }
  .headline {
    position: absolute; top: 142px; left: 0; right: 0;
    font-weight: 300; text-transform: uppercase;
    font-size: 37px; line-height: 46px;
  }
  .headline .spaced { letter-spacing: 3.4px; }
  .headline .accent { color: var(--gold); font-weight: 700; letter-spacing: 2px; }
  .headline .win { font-style: italic; }
  .headline .condensed {
    font-family: "Open Sans Condensed", "Open Sans", Arial, sans-serif;
    font-weight: 300; font-size: 40px; letter-spacing: 0;
    transform: scaleX(0.98);
  }
  .coaster {
    position: absolute; left: 207px; top: 331px;
    width: 434px; height: 434px;
  }
  .coaster-text {
    position: absolute; left: 0; right: 0; top: 183px;
    color: var(--stamp);
  }
  .coaster-title {
    font-family: "Lobster", cursive;
    font-size: 68px; line-height: 70px;
    text-shadow: 0 1px 0 rgba(255,220,150,0.35);
  }
  .coaster-sub {
    font-family: "Montserrat", Arial, sans-serif; font-weight: 700;
    font-size: 25px; letter-spacing: 2px; text-transform: uppercase;
    text-shadow: 0 1px 0 rgba(255,220,150,0.35);
  }
  .intro {
    position: absolute; top: 765px; left: 0; right: 0;
    font-size: 18.5px; font-weight: 400; line-height: 24px;
  }
  .call {
    position: absolute; top: 799px; left: 0; right: 0;
    font-size: 37px; font-weight: 300; text-transform: uppercase; line-height: 46px;
  }
  .call strong { color: var(--gold); font-weight: 700; }
  .style-note {
    position: absolute; top: 891px; left: 0; right: 0;
    font-size: 22px; font-weight: 600; color: var(--gold); line-height: 28px;
  }
  .nose {
    position: absolute; top: 917px; left: 0; right: 0;
    font-size: 55px; font-weight: 300; color: var(--gold);
    text-transform: uppercase; line-height: 68px;
  }
  .nose strong { color: var(--white); font-weight: 700; }
  .footer-band {
    position: absolute; left: 0; right: 0; top: 1022px; height: 114px;
    background:
      linear-gradient(180deg, rgba(0,0,0,0.55) 0%, rgba(0,0,0,0) 12%, rgba(0,0,0,0) 88%, rgba(0,0,0,0.55) 100%),
      radial-gradient(ellipse at 50% 70%, var(--band-light) 0%, #5e4420 55%, var(--band-dark) 100%);
    border-top: 2px solid #7a5a28; border-bottom: 2px solid #7a5a28;
    display: flex; align-items: center; justify-content: center; gap: 6px;
    font-size: 19px; color: #f1ece0; letter-spacing: -0.3px;
  }
  .footer-band .lead {
    font-family: "Lobster", cursive; color: var(--gold); font-size: 21px;
  }
</style>
</head>
<body>
<div class="poster">
  <div class="panel">
    <div class="light-streaks" role="img" aria-label="Diagonal soft coloured light streaks behind the badge"></div>

    <div class="brand"><span class="brand-dot"></span>The Brewhouse Kestrelgate</div>

    <h1 class="headline">
      <div class="spaced">Submit your idea for the name</div>
      <div class="spaced">of our <span class="accent">newest craft beer,</span> <span class="win">win</span>,</div>
      <div class="condensed">And see your name go down in history!</div>
    </h1>

    <div class="coaster">
      <svg width="434" height="434" viewBox="0 0 434 434" aria-hidden="true">
        <defs>
          <radialGradient id="leather" cx="45%" cy="40%" r="65%">
            <stop offset="0%" stop-color="var(--leather-light)"/>
            <stop offset="65%" stop-color="var(--leather-mid)"/>
            <stop offset="100%" stop-color="var(--leather-dark)"/>
          </radialGradient>
        </defs>
        <circle cx="217" cy="217" r="216" fill="url(#leather)"/>
        <circle cx="217" cy="217" r="204" fill="none" stroke="var(--stamp)" stroke-width="1.6" stroke-dasharray="7 5" opacity="0.8"/>
      </svg>
      <div class="coaster-text">
        <div class="coaster-title">Your Name</div>
        <div class="coaster-sub">On a beer label!</div>
      </div>
    </div>

    <p class="intro">I am the newest addition to The Brewhouse Kestrelgate beer family</p>
    <p class="call">And I am looking for a <strong>name!</strong></p>

    <p class="style-note">I am a porter style with deep, rich chocolaty flavours and</p>
    <p class="nose">A roasted malt <strong>nose</strong></p>

    <div class="footer-band">
      <span class="lead">Get involved!</span>
      <span>Help me find a name and get your name put on the badge as well!</span>
    </div>
  </div>
</div>
</body>
</html>
```